Pellmore Heating & Air

I need a business card made for my company. I would like my new logo for Pellmore Heating and Air on the front and my Garage Door on the back.
Front to say -Heating & Air Conditioning , Mini Splits and Heat Pumps, Hydronic In-Floor Heat. Locally Owned and Operated! Licensed, Boned and Insured. Free Estimates on new equipment. 555-201-4837
KVB Back Card, change phone# to 555-318-6024. Remove Commercial and residential and fully sticked vans lines.

```html
<!DOCTYPE html>
<html lang="en">
<head>
<meta charset="utf-8">
<title>Pellmore Heating &amp; Air – Business Cards</title>
<link rel="stylesheet" href="https://fonts.googleapis.com/css2?family=Montserrat:wght@500;600;700;800&display=swap">
<style>
  :root {
    --bg: #e9eaec;
    --card-white: #ffffff;
    --brand-blue: #17528c;
    --brand-red: #e2261f;
    --text-light: #ffffff;
  }
  * { margin: 0; padding: 0; box-sizing: border-box; }
  html, body { width: 1200px; height: 900px; overflow: hidden; }
  body {
    background: var(--bg);
    font-family: "Montserrat", sans-serif;
    display: flex;
    flex-direction: column;
    align-items: center;
    justify-content: center;
    gap: 34px;
  }
  .card {
    width: 700px;
    height: 400px;
    border-radius: 26px;
    overflow: hidden;
    display: flex;
    background: var(--card-white);
    box-shadow: 0 6px 18px rgba(0,0,0,0.18);
  }
  .card__brand {
    flex: 0 0 42%;
    display: flex;
    align-items: center;
    justify-content: center;
    padding: 24px;
  }
  .card__info {
    flex: 1;
    background: var(--brand-blue);
    color: var(--text-light);
    padding: 40px 38px;
    display: flex;
    flex-direction: column;
    justify-content: center;
  }
  .wordmark {
    display: flex;
    align-items: center;
    gap: 12px;
    color: var(--brand-blue);
    font-weight: 800;
    text-transform: uppercase;
    line-height: 1.1;
  }
  .wordmark__dot {
    flex: 0 0 22px;
    height: 22px;
    border-radius: 50%;
    background: var(--brand-red);
  }
  .wordmark--heating { font-size: 27px; }
  .wordmark--garage { font-size: 30px; }
  .service-list { list-style: none; }
  .service-list li {
    position: relative;
    padding-left: 16px;
    font-weight: 600;
    font-size: 17px;
    line-height: 1.55;
  }
  .service-list li::before {
    content: "";
    position: absolute;
    left: 0;
    top: 10px;
    width: 6px;
    height: 6px;
    border-radius: 50%;
    background: var(--brand-red);
  }
  .tagline {
    margin-top: 14px;
    font-weight: 600;
    font-size: 19px;
    line-height: 1.3;
  }
  .estimate {
    margin-top: 12px;
    font-weight: 700;
    font-size: 16px;
  }
  .phone-large {
    margin-top: 4px;
    font-weight: 700;
    font-size: 32px;
    letter-spacing: 0.5px;
  }
  .save-heading {
    color: var(--brand-red);
    font-weight: 700;
    font-size: 27px;
    letter-spacing: 1px;
    text-transform: uppercase;
    margin-bottom: 12px;
  }
  .contact-list { list-style: none; margin-bottom: 10px; }
  .contact-list li {
    display: flex;
    align-items: center;
    gap: 10px;
    font-weight: 500;
    font-size: 19px;
    line-height: 1.5;
  }
  .contact-list svg { width: 16px; height: 16px; flex: 0 0 16px; }
  .card--garage .service-list li { font-weight: 500; font-size: 19px; }
</style>
</head>
<body>

  <section class="card card--heating">
    <div class="card__brand">
      <div class="wordmark wordmark--heating">
        <span class="wordmark__dot"></span>
        <span>Pellmore<br>Heating &amp; Air</span>
      </div>
    </div>
    <div class="card__info">
      <ul class="service-list">
        <li>Heating &amp; Air Conditioning</li>
        <li>Mini Splits and Heat Pumps</li>
        <li>Hydronic In-Floor Heat</li>
      </ul>
      <p class="tagline">Locally Owned and Operated!<br>Licensed, Boned and Insured.</p>
      <p class="estimate">Free Estimates On New Equipment.</p>
      <p class="phone-large">555-201-4837</p>
    </div>
  </section>

  <section class="card card--garage">
    <div class="card__brand">
      <div class="wordmark wordmark--garage">
        <span class="wordmark__dot"></span>
        <span>KVB<br>Garage Door</span>
      </div>
    </div>
    <div class="card__info">
      <h2 class="save-heading">Save This Card!</h2>
      <ul class="contact-list">
        <li>
          <svg viewBox="0 0 24 24" aria-hidden="true"><path fill="#e2261f" d="M6.6 10.8a15.1 15.1 0 0 0 6.6 6.6l2.2-2.2c.3-.3.7-.4 1-.2 1.1.4 2.3.6 3.6.6.6 0 1 .4 1 1V20c0 .6-.4 1-1 1C10.6 21 3 13.4 3 4c0-.6.4-1 1-1h3.5c.6 0 1 .4 1 1 0 1.3.2 2.5.6 3.6.1.3 0 .7-.2 1z"/></svg>
          555-318-6024
        </li>
        <li>
          <svg viewBox="0 0 24 24" aria-hidden="true"><path fill="#e2261f" d="M3 5h18a1 1 0 0 1 1 1v12a1 1 0 0 1-1 1H3a1 1 0 0 1-1-1V6a1 1 0 0 1 1-1zm9 7 8-5H4z"/></svg>
          kvbgaragedoor@mail.com
        </li>
        <li>
          <svg viewBox="0 0 24 24" aria-hidden="true"><circle cx="12" cy="12" r="9" fill="none" stroke="#e2261f" stroke-width="2"/><path d="M3 12h18M12 3c3 3 3 15 0 18M12 3c-3 3-3 15 0 18" fill="none" stroke="#e2261f" stroke-width="1.6"/></svg>
          www.KVBGarageDoor.com
        </li>
      </ul>
      <ul class="service-list">
        <li>Same Day &amp; Emergency Service</li>
        <li>All Major Brands</li>
        <li>Locally Owned &amp; Operated</li>
      </ul>
    </div>
  </section>

</body>
</html>
```